Process Flow Chart for Real Estate Agency

We need a visual flow chart of the process of selling a home for our Real Estate Agency. This visual will be provided to all new staff to explain the process and also to potential clients to explain how detailed the process is. It needs to show each step as detailed in the attached word doc and use icons and arrows to show the direction of flow.

Target Market(s)

Staff & Potential Clients

Industry/Entity Type

Real Estate

Font styles to use
Sans Serif

Colors

Designer to choose colors to be used in the design.

Requirements
Must have
• Easy to read, lots of icons, colour coded with Agent in one colour, Admin in another (some tasks are either/or so not sure what to colour those ones.)
Nice to have
• Include one of the two attached logos

```html
<!DOCTYPE html>
<html lang="en">
<head>
<meta charset="utf-8">
<title>Selling A Home – Harbourline Real Estate</title>
<link rel="stylesheet" href="https://fonts.googleapis.com/css2?family=Arimo:ital,wght@1,700&family=Tinos:wght@400;700&display=swap">
<style>
  :root {
    --admin: #e47c22;
    --agent: #2e3192;
    --either: #1d8a3e;
    --ink: #111111;
    --paper: #ffffff;
    --screen: #e6e6e6;
    --grid: #8fa8d8;
    --calendar-head: #3a3d99;
  }
  * { box-sizing: border-box; margin: 0; padding: 0; }
  html, body { width: 1200px; height: 819px; overflow: hidden; background: var(--paper); }
  .canvas {
    position: relative; width: 1200px; height: 819px; overflow: hidden;
    background: var(--paper); color: var(--ink);
    font-family: "Tinos", "Times New Roman", serif; font-weight: 700;
  }
  .abs { position: absolute; }
  .flow-arrows { position: absolute; inset: 0; width: 1200px; height: 819px; }

  .legend { left: 8px; top: 18px; font-size: 16px; line-height: 22px; }
  .legend .admin { color: var(--admin); }
  .legend .agent { color: var(--agent); }
  .legend .either { color: var(--either); }

  .title {
    left: 380px; top: 6px; width: 420px; text-align: center;
    font-family: "Arimo", Arial, sans-serif; font-style: italic; font-weight: 700;
    font-size: 50px; line-height: 56px;
  }

  .brand { left: 905px; top: 22px; width: 260px; color: var(--agent); font-weight: 700; }
  .brand-dot { position: absolute; left: 100px; top: 0; width: 34px; height: 34px; border-radius: 50%; background: var(--agent); }
  .brand-name { position: absolute; left: 0; top: 36px; font-size: 36px; line-height: 38px; }
  .brand-sub { position: absolute; left: 0; top: 76px; font-size: 20px; line-height: 22px; }

  .step-text { position: absolute; text-align: center; font-size: 13.5px; line-height: 16px; }
  .on-dark { color: var(--paper); }

  .device { position: absolute; }
  .device svg { position: absolute; inset: 0; width: 100%; height: 100%; }
  .device .step-text { z-index: 1; }

  .people-icon { position: absolute; border-radius: 10px; background: linear-gradient(#3d44a8, var(--agent)); }
  .lettering { position: absolute; background: linear-gradient(135deg, #6a74c9, var(--agent)); border-radius: 6px; }

  .agent-box { left: 1038px; top: 595px; width: 151px; height: 122px; background: var(--agent); border: 1px solid var(--ink); }
  .checklist-box { left: 647px; top: 617px; width: 112px; height: 147px; border: 1px solid var(--ink); background: var(--paper); }
  .checklist-label { position: absolute; left: 48px; top: 6px; font-size: 7px; font-weight: 700; }

  .next-page { left: 112px; top: 762px; font-size: 20px; font-weight: 400; }
</style>
</head>
<body>
<main class="canvas">

  <svg class="flow-arrows" viewBox="0 0 1200 819" aria-hidden="true">
    <defs>
      <marker id="head" viewBox="0 0 10 10" refX="5" refY="5" markerWidth="4" markerHeight="4" orient="auto">
        <path d="M0,0 L10,5 L0,10 z" fill="#111"/>
      </marker>
      <marker id="head-big" viewBox="0 0 10 10" refX="5" refY="5" markerWidth="3" markerHeight="3" orient="auto">
        <path d="M0,0 L10,5 L0,10 z" fill="#111"/>
      </marker>
      <marker id="head-green" viewBox="0 0 10 10" refX="5" refY="5" markerWidth="4" markerHeight="4" orient="auto">
        <path d="M0,0 L10,5 L0,10 z" fill="#1d8a3e"/>
      </marker>
    </defs>
    <g stroke="#111" stroke-width="5" fill="none" marker-end="url(#head)" stroke-linecap="round">
      <path d="M139,173 L188,173"/>
      <path d="M267,173 L319,173"/>
      <path d="M412,173 L465,173"/>
      <path d="M687,165 Q715,172 741,167"/>
      <path d="M872,398 L819,398"/>
      <path d="M656,352 L604,352"/>
      <path d="M440,323 L379,323"/>
      <path d="M164,472 L212,472"/>
      <path d="M361,451 Q400,452 427,463"/>
      <path d="M551,517 Q590,518 619,508"/>
      <path d="M712,502 L774,502"/>
      <path d="M947,483 L990,483"/>
      <path d="M1022,647 L970,647"/>
      <path d="M792,656 L764,656"/>
      <path d="M638,694 L585,694"/>
      <path d="M422,657 L374,655"/>
      <path d="M206,620 L154,610"/>
    </g>
    <g stroke="#111" stroke-width="11" fill="none" marker-end="url(#head-big)" stroke-linecap="round">
      <path d="M880,184 C930,150 978,170 990,206"/>
      <path d="M1125,312 C1152,340 1140,368 1064,372"/>
      <path d="M220,323 C182,320 145,332 130,356"/>
      <path d="M1098,490 C1140,510 1160,548 1155,588"/>
      <path d="M55,672 C35,720 52,770 88,798"/>
    </g>
    <polyline points="248,394 290,352 312,366 360,314" stroke="#1d8a3e" stroke-width="4" fill="none" marker-end="url(#head-green)"/>
  </svg>

  <div class="abs legend">
    <div><span class="admin">Orange Icons</span> - Admin tasks</div>
    <div><span class="agent">Blue Icons</span> - Agent Tasks</div>
    <div><span class="either">Green Icons</span> - Either Agent or Admin tasks</div>
  </div>

  <h1 class="abs title">Selling A Home</h1>

  <div class="abs brand" aria-label="Harbourline Real Estate">
    <span class="brand-dot"></span>
    <span class="brand-name">Harbourline</span>
    <span class="brand-sub">Real Estate</span>
  </div>

  <!-- Row 1 -->
  <div class="device phone" style="left:35px;top:125px;width:99px;height:180px;">
    <svg viewBox="0 0 99 180" preserveAspectRatio="none">
      <rect x="1" y="1" width="97" height="178" rx="16" fill="var(--agent)" stroke="#111"/>
      <rect x="8" y="8" width="83" height="150" rx="10" fill="var(--screen)"/>
      <circle cx="49.5" cy="169" r="6" fill="var(--paper)" stroke="#111"/>
    </svg>
    <div class="step-text" style="left:10px;top:20px;width:79px;">Agent calls potential client to arrange meeting and obtain details about the property.</div>
  </div>

  <div class="people-icon" role="img" aria-label="Two people meeting icon" style="left:204px;top:138px;width:50px;height:54px;"></div>
  <div class="step-text" style="left:166px;top:198px;width:124px;">Agent ensures all decision makers will be present at the meeting.</div>

  <div class="device phone" style="left:338px;top:128px;width:65px;height:139px;">
    <svg viewBox="0 0 65 139" preserveAspectRatio="none">
      <rect x="1" y="1" width="63" height="137" rx="12" fill="var(--agent)" stroke="#111"/>
      <rect x="6" y="6" width="53" height="115" rx="8" fill="var(--screen)"/>
      <circle cx="32.5" cy="130" r="4.5" fill="var(--paper)" stroke="#111"/>
    </svg>
    <div class="step-text" style="left:4px;top:12px;width:57px;">Agent adds Vendors contact details on phone</div>
  </div>

  <div class="device calendar" style="left:489px;top:128px;width:181px;height:165px;">
    <svg viewBox="0 0 181 165" preserveAspectRatio="none">
      <rect x="1" y="1" width="179" height="163" fill="var(--calendar-head)" stroke="#111"/>
      <rect x="10" y="45" width="161" height="112" fill="var(--grid)" stroke="#111"/>
      <rect x="29" y="10" width="120" height="26" fill="var(--paper)" stroke="#111"/>
      <g fill="var(--paper)" stroke="#111" stroke-width="0.6">
        <rect x="150" y="50" width="10" height="9"/><rect x="163" y="50" width="10" height="9"/>
        <rect x="14" y="68" width="16" height="12"/><rect x="35" y="68" width="16" height="12"/><rect x="56" y="68" width="16" height="12"/>
        <rect x="14" y="90" width="16" height="12"/><rect x="35" y="90" width="16" height="12"/><rect x="56" y="90" width="16" height="12"/>
        <rect x="14" y="112" width="16" height="12"/><rect x="35" y="112" width="16" height="12"/><rect x="56" y="112" width="16" height="12"/>
        <rect x="14" y="132" width="16" height="12"/><rect x="35" y="132" width="16" height="12"/><rect x="56" y="132" width="16" height="12"/>
        <rect x="77" y="132" width="16" height="12"/><rect x="98" y="132" width="16" height="12"/><rect x="119" y="132" width="16" height="12"/>
        <rect x="140" y="132" width="16" height="12"/><rect x="160" y="132" width="12" height="12"/>
        <rect x="14" y="150" width="16" height="6"/>
      </g>
      <rect x="69" y="56" width="86" height="64" fill="var(--paper)" stroke="#111"/>
      <text x="89" y="27" font-family="Tinos, serif" font-weight="700" font-size="11" fill="var(--agent)">Harbourline</text>
    </svg>
    <div class="step-text" style="left:70px;top:60px;width:84px;font-size:12.5px;line-height:15px;">Agent adds appointment to personal calendar</div>
  </div>

  <div class="lettering" role="img" aria-label="Thank You lettering" style="left:742px;top:120px;width:72px;height:70px;"></div>
  <div class="step-text" style="left:704px;top:197px;width:168px;">Agent sends SMS to potential client thanking them for the opportunity</div>

  <div class="device laptop" style="left:1012px;top:183px;width:165px;height:126px;">
    <svg viewBox="0 0 165 126" preserveAspectRatio="none">
      <rect x="4" y="1" width="157" height="96" rx="5" fill="var(--either)" stroke="#111"/>
      <rect x="10" y="6" width="145" height="84" rx="6" fill="var(--paper)" stroke="#111"/>
      <polygon points="6,98 159,98 164,124 1,124" fill="var(--either)" stroke="#111"/>
      <rect x="68" y="110" width="28" height="9" fill="var(--paper)" stroke="#111"/>
    </svg>
    <div class="step-text" style="left:10px;top:10px;width:145px;text-align:left;padding-left:4px;">Agent/Admin orders ARE from Ashworth's</div>
  </div>

  <!-- Row 2 -->
  <div class="device laptop" style="left:872px;top:291px;width:178px;height:117px;">
    <svg viewBox="0 0 178 117" preserveAspectRatio="none">
      <rect x="4" y="1" width="170" height="90" rx="5" fill="var(--agent)" stroke="#111"/>
      <rect x="10" y="6" width="158" height="78" rx="6" fill="var(--paper)" stroke="#111"/>
      <polygon points="6,92 172,92 177,115 1,115" fill="var(--agent)" stroke="#111"/>
      <rect x="74" y="102" width="30" height="8" fill="var(--paper)" stroke="#111"/>
    </svg>
    <div class="step-text" style="left:14px;top:10px;width:150px;">Agent Completes TMP to provide Admin for Preplist-ing Kit</div>
  </div>

  <div class="device envelope" style="left:662px;top:298px;width:146px;height:159px;">
    <svg viewBox="0 0 146 159" preserveAspectRatio="none">
      <rect x="1" y="1" width="144" height="157" fill="var(--admin)" stroke="#111"/>
      <polyline points="1,1 73,48 145,1" fill="none" stroke="#111"/>
    </svg>
    <div class="step-text" style="left:40px;top:3px;width:66px;font-size:9px;line-height:10px;font-weight:400;">Prep-Lisiting Kit</div>
    <div class="step-text" style="left:6px;top:28px;width:134px;text-align:justify;font-size:13px;line-height:16px;">AdminPrepares Pre-listing Kit with Questionaire, sample brochure &amp; cover letter, property magazine, agent profile book</div>
  </div>

  <div class="device envelope" style="left:452px;top:300px;width:136px;height:131px;">
    <svg viewBox="0 0 136 131" preserveAspectRatio="none">
      <rect x="1" y="1" width="134" height="129" fill="var(--either)" stroke="#111"/>
      <polyline points="1,1 68,40 135,1" fill="none" stroke="#111"/>
    </svg>
    <div class="step-text" style="left:34px;top:3px;width:68px;font-size:9px;line-height:10px;font-weight:400;">Prep-Lisiting Kit</div>
    <div class="step-text on-dark" style="left:4px;top:32px;width:128px;">Agent/Admin delivers pre-listing Kit (preferably within the hr) &amp; SMS potential Vendor</div>
  </div>

  <div class="step-text" style="left:222px;top:277px;width:152px;">Admin/Agent to research &amp; print comparable Sales Reports</div>

  <!-- Row 3 -->
  <div class="device envelope" style="left:16px;top:368px;width:143px;height:166px;">
    <svg viewBox="0 0 143 166" preserveAspectRatio="none">
      <rect x="1" y="1" width="141" height="164" fill="var(--admin)" stroke="#111"/>
      <polyline points="1,1 71.5,38 142,1" fill="none" stroke="#111"/>
    </svg>
    <div class="step-text" style="left:46px;top:5px;width:51px;font-size:9px;line-height:10px;font-weight:400;">TMP</div>
    <div class="step-text" style="left:4px;top:38px;width:135px;font-size:13px;line-height:16.5px;">Admin to prepare TMP with Marketing Costs Selection Booklet, Service Offering Selection Booklet, Sales Agency Agreement &amp; Benefits Form, ARE</div>
  </div>

  <div class="device laptop" style="left:223px;top:408px;width:138px;height:112px;">
    <svg viewBox="0 0 138 112" preserveAspectRatio="none">
      <rect x="4" y="1" width="130" height="86" rx="5" fill="var(--admin)" stroke="#111"/>
      <rect x="10" y="6" width="118" height="74" rx="6" fill="var(--paper)" stroke="#111"/>
      <polygon points="6,88 132,88 137,110 1,110" fill="var(--admin)" stroke="#111"/>
      <rect x="55" y="97" width="28" height="8" fill="var(--paper)" stroke="#111"/>
    </svg>
    <div class="step-text" style="left:12px;top:6px;width:116px;text-align:left;">Admin enters potntial Vendor in CRM &amp; set Ápraisal"track</div>
  </div>

  <div class="device phone" style="left:464px;top:436px;width:78px;height:159px;">
    <svg viewBox="0 0 78 159" preserveAspectRatio="none">
      <rect x="1" y="1" width="76" height="157" rx="14" fill="var(--agent)" stroke="#111"/>
      <rect x="7" y="7" width="64" height="130" rx="9" fill="var(--screen)"/>
      <circle cx="39" cy="148" r="5" fill="var(--paper)" stroke="#111"/>
    </svg>
    <div class="step-text" style="left:6px;top:14px;width:66px;">Agent confirms appraisal on morning of appoint-ment via SMS</div>
  </div>

  <div class="people-icon" role="img" aria-label="Two people meeting icon" style="left:638px;top:466px;width:50px;height:54px;"></div>
  <div class="step-text" style="left:598px;top:527px;width:136px;">Agent meets with potential vendor and completes appraisal</div>

  <div class="device laptop" style="left:789px;top:464px;width:151px;height:113px;">
    <svg viewBox="0 0 151 113" preserveAspectRatio="none">
      <rect x="4" y="1" width="143" height="86" rx="5" fill="var(--admin)" stroke="#111"/>
      <rect x="10" y="6" width="131" height="74" rx="6" fill="var(--paper)" stroke="#111"/>
      <polygon points="6,88 145,88 150,111 1,111" fill="var(--admin)" stroke="#111"/>
      <rect x="62" y="97" width="28" height="8" fill="var(--paper)" stroke="#111"/>
    </svg>
    <div class="step-text" style="left:12px;top:10px;width:128px;text-align:left;">Admin prepares written appraisal and delivers with vouchers/gift</div>
  </div>

  <div class="people-icon" role="img" aria-label="Two people meeting icon" style="left:1008px;top:428px;width:47px;height:50px;"></div>
  <div class="step-text" style="left:972px;top:486px;width:118px;">Agent hand delivers report and voucher/ chocolates</div>

  <!-- Row 4 -->
  <div class="abs agent-box">
    <div class="step-text on-dark" style="left:4px;top:6px;width:142px;font-weight:400;">Agent recieves confir-mation from Vendor to proceed with listing &amp; arranges signing of Residential Sales Agency Agreement</div>
  </div>

  <div class="device laptop" style="left:818px;top:609px;width:166px;height:118px;">
    <svg viewBox="0 0 166 118" preserveAspectRatio="none">
      <rect x="4" y="1" width="158" height="90" rx="5" fill="var(--admin)" stroke="#111"/>
      <rect x="10" y="6" width="146" height="78" rx="6" fill="var(--paper)" stroke="#111"/>
      <polygon points="6,92 160,92 165,116 1,116" fill="var(--admin)" stroke="#111"/>
      <rect x="69" y="102" width="28" height="8" fill="var(--paper)" stroke="#111"/>
    </svg>
    <div class="step-text" style="left:12px;top:10px;width:130px;text-align:left;">Admin checkes residential Sales Agency &amp; enters listing into CRM</div>
  </div>

  <div class="abs checklist-box">
    <svg style="position:absolute;left:44px;top:4px;width:40px;height:36px;" viewBox="0 0 40 36" aria-hidden="true">
      <path d="M8,20 L17,30 L36,3" fill="none" stroke="var(--admin)" stroke-width="4" stroke-linecap="round" stroke-linejoin="round"/>
    </svg>
    <span class="checklist-label">Checklist</span>
    <div class="step-text" style="left:4px;top:18px;width:100px;text-align:left;font-weight:400;font-size:14px;line-height:17px;">Admin<br>completes the “New Listing Checklist”and prepares black folder</div>
  </div>

  <div class="device laptop" style="left:439px;top:628px;width:170px;height:113px;">
    <svg viewBox="0 0 170 113" preserveAspectRatio="none">
      <rect x="4" y="1" width="162" height="86" rx="5" fill="var(--admin)" stroke="#111"/>
      <rect x="10" y="6" width="150" height="74" rx="6" fill="var(--paper)" stroke="#111"/>
      <polygon points="6,88 164,88 169,111 1,111" fill="var(--admin)" stroke="#111"/>
      <rect x="71" y="97" width="28" height="8" fill="var(--paper)" stroke="#111"/>
    </svg>
    <div class="step-text" style="left:12px;top:10px;width:146px;text-align:left;">Admin checks Vendor email address &amp; if required call or SMS to obtain</div>
  </div>

  <div class="device laptop" style="left:216px;top:563px;width:164px;height:117px;">
    <svg viewBox="0 0 164 117" preserveAspectRatio="none">
      <rect x="4" y="1" width="156" height="90" rx="5" fill="var(--admin)" stroke="#111"/>
      <rect x="10" y="6" width="144" height="78" rx="6" fill="var(--paper)" stroke="#111"/>
      <polygon points="6,92 158,92 163,115 1,115" fill="var(--admin)" stroke="#111"/>
      <rect x="68" y="101" width="28" height="8" fill="var(--paper)" stroke="#111"/>
    </svg>
    <div class="step-text" style="left:12px;top:10px;width:144px;text-align:left;font-size:12.5px;line-height:15.5px;">Admin set track (New lisiting 1) as at date of signing sales agency &amp; removes appraisal track</div>
  </div>

  <div class="device laptop" style="left:19px;top:563px;width:154px;height:103px;">
    <svg viewBox="0 0 154 103" preserveAspectRatio="none">
      <rect x="4" y="1" width="146" height="78" rx="5" fill="var(--admin)" stroke="#111"/>
      <rect x="10" y="6" width="134" height="66" rx="6" fill="var(--paper)" stroke="#111"/>
      <polygon points="6,80 148,80 153,101 1,101" fill="var(--admin)" stroke="#111"/>
      <rect x="63" y="88" width="28" height="8" fill="var(--paper)" stroke="#111"/>
    </svg>
    <div class="step-text" style="left:12px;top:10px;width:130px;text-align:left;">Admin completes the marketing section of CRM</div>
  </div>

  <div class="abs next-page">Next Page</div>
</main>
</body>
</html>
```